Government Contracting business needs a website design.

Brisco & Wendell, LLC is a minority owned Service Disabled Veteran Owned Small Business (SDVOSB) that provides Strategic Planning, Public Health Emergency Response, and Data Management Solutions for Federal Civilian and Defense Agencies. We have over 20 years of experience helping health and defense agencies develop concept of operations, deploy assets and personnel in Hot Zones around the world, and deliver goods and services all of the globe.

We are a leader in the field of Data Management. We help our customers develop cloud migration and disaster recovery strategies. We are experts with database management, data replication, queries, consolidation, and records management.

We are looking for a very nice and simple website designs that states clearly what we do as a company and that is easy for our customers to follow. We would like to have some moving pictures that are base on our expertise. We want the website to be easy to use and have the scroll down features that keeps things all on the same page when clicking on the menu. I attached a document with what we need on the website. I will also attach our logo. We want it to look simple clean and very professional.

Target Market(s)

Government Contracting, Management Consulting, Health

Industry/Entity Type

Government

Coding

Coded - Design and coding required

Number of Pages Required

1 page

Font styles to use
Serif

Requirements
Must have
• Very nice picture slides that speaks to our capabilities in Disaster Response, Strategic Planning, and Database Management. Slick look and design. Make sure SDVOSB Logo is right at the beginning of website as our customers is looking for that certification. Very nice colors that blend well with our logo.
Nice to have
• Very nice and slick colors that blends well with logo.
Should not have
• Basic website design that are weary on the eye. No bright colors, just simple colors that looks good with logo.

```html
<!DOCTYPE html>
<html lang="en">
<head>
<meta charset="utf-8">
<title>Brisco &amp; Wendell, LLC</title>
<link rel="stylesheet" href="https://fonts.googleapis.com/css2?family=Poppins:ital,wght@0,400;0,500;0,600;0,700;1,400&family=Libre+Baskerville&display=swap">
<style>
:root{
  --navy:#1f3f5c;
  --ink:#111418;
  --text:#2b2f33;
  --muted:#555b61;
  --white:#ffffff;
  --plum:#4b2a57;
  --teal:#1b5473;
  --hero-dark:#1e2633;
  --hero-mid:#4a5566;
}
*{margin:0;padding:0;box-sizing:border-box}
html,body{width:1200px;height:2791px;overflow:hidden}
body{font-family:'Poppins',sans-serif;color:var(--text);background:var(--white);position:relative}
.site-header{position:absolute;top:0;left:0;width:1200px;height:75px;background:rgba(15,18,24,.88);z-index:3}
.brand{position:absolute;left:160px;top:22px;display:flex;align-items:center;gap:10px;color:var(--white);font-family:'Libre Baskerville',serif;font-size:19px}
.brand-mark{width:28px;height:28px;border:2px solid var(--white)}
.main-nav{position:absolute;left:478px;top:29px;display:flex;gap:24px;font-size:12.5px;line-height:16px;color:var(--white);white-space:nowrap}
.cert-badge{position:absolute;left:982px;top:9px;width:56px;height:56px;border-radius:50%;background:var(--white);border:4px solid #cfd6e3}
.hero{position:absolute;top:0;left:0;width:1200px;height:601px;background:linear-gradient(120deg,var(--hero-dark) 0%,var(--hero-mid) 45%,#8b8f97 60%,#2a3140 100%)}
.hero-title{position:absolute;left:160px;top:290px;color:var(--white);font-weight:700;font-size:44px;line-height:52px;text-shadow:0 2px 6px rgba(0,0,0,.4)}
.hero-arrow{position:absolute;top:335px;width:24px;height:40px}
.about{position:absolute;top:601px;left:0;width:1200px;height:489px;background:linear-gradient(180deg,#e4e4e5,#f3f3f4);overflow:hidden}
.section-title{font-weight:600;font-size:30px;color:var(--ink)}
.about .section-title{position:absolute;left:162px;top:128px}
.about-text{position:absolute;left:162px;top:187px;width:406px;font-size:10.8px;line-height:21.8px;color:var(--text)}
.btn{position:absolute;display:flex;align-items:center;justify-content:center;border:2px solid var(--navy);border-radius:20px;color:var(--navy);font-size:13px;font-weight:500;background:transparent}
.about .btn{left:162px;top:356px;width:106px;height:36px}
.about-art{position:absolute;left:600px;top:106px;width:495px;height:383px;background:linear-gradient(135deg,#d9dcde,#c5cbd0 50%,#e8e9ea)}
.capabilities{position:absolute;top:1090px;left:0;width:1200px;height:575px;background:var(--white);overflow:hidden}
.deco-ring{position:absolute;left:-230px;top:-40px;width:540px;height:540px;border-radius:50%;border:70px solid #f2f2f3}
.capabilities .section-title{position:absolute;top:55px;width:1200px;text-align:center}
.card{position:absolute;top:145px;width:278px;height:308px;background:var(--white);box-shadow:0 2px 10px rgba(0,0,0,.18);text-align:center}
.card svg{margin-top:38px;width:88px;height:80px}
.card h3{font-weight:500;font-size:18px;color:var(--ink);margin-top:14px}
.card p{font-size:10.8px;line-height:24px;color:var(--muted);padding:0 30px;margin-top:12px}
.leadership{position:absolute;top:1665px;left:0;width:1200px;height:500px;background:linear-gradient(90deg,var(--plum),#2e3a63 45%,var(--teal));color:var(--white)}
.leadership .section-title{position:absolute;top:55px;width:1200px;text-align:center;color:var(--white);font-weight:400;font-size:32px}
.leader-photo{position:absolute;top:152px;width:156px;height:263px;background:linear-gradient(180deg,#f4f4f4,#d3d6da)}
.leader-info{position:absolute;top:155px;width:248px}
.leader-info h3{font-weight:600;font-size:16px}
.leader-info .role{font-style:italic;font-size:11px;margin-top:10px}
.leader-info p{font-size:10.4px;line-height:20.8px;margin-top:10px;text-align:justify}
.join{position:absolute;top:2165px;left:0;width:1200px;height:417px;background:linear-gradient(180deg,#ffffff,#e3e4e6)}
.join .section-title{position:absolute;top:105px;width:1200px;text-align:center}
.join-text{position:absolute;left:236px;top:165px;width:728px;text-align:center;font-size:10.8px;line-height:21.6px;color:var(--text)}
.join .btn{left:546px;top:295px;width:108px;height:36px}
.site-footer{position:absolute;top:2582px;left:0;width:1200px;height:209px;background:var(--white);text-align:center}
.footer-brand{position:absolute;left:0;width:1200px;top:45px;display:flex;justify-content:center;align-items:center;gap:10px;font-family:'Libre Baskerville',serif;font-size:19px;color:var(--ink)}
.footer-brand .brand-mark{border-color:var(--ink)}
.social{position:absolute;top:108px;left:0;width:1200px;display:flex;justify-content:center;gap:14px}
.social span{width:22px;height:22px;border-radius:50%;background:var(--ink)}
.copyright{position:absolute;top:155px;width:1200px;font-size:12px;color:var(--text)}
</style>
</head>
<body>
<header class="site-header">
  <div class="brand"><span class="brand-mark"></span>Brisco &amp; Wendell</div>
  <nav class="main-nav"><span>Home</span><span>About Us</span><span>Services</span><span>Why Hire Us?</span><span>Our Partners</span><span>Contact</span></nav>
  <div class="cert-badge" role="img" aria-label="SDVOSB certification badge"></div>
</header>

<section class="hero" role="img" aria-label="Photo of business professionals reviewing documents with a pen">
  <h1 class="hero-title">WELCOME TO<br>BRISCOWENDELL</h1>
  <svg class="hero-arrow" style="left:14px" viewBox="0 0 24 40"><path d="M20 4 4 20l16 16" fill="none" stroke="#fff" stroke-width="2"/></svg>
  <svg class="hero-arrow" style="left:1150px" viewBox="0 0 24 40"><path d="M4 4l16 16L4 36" fill="none" stroke="#fff" stroke-width="2"/></svg>
</section>

<section class="about">
  <h2 class="section-title">ABOUT US</h2>
  <p class="about-text">Brisco &amp; Wendell, LLC is a minority owned Service Disabled Veteran Owned Small Business (SDVOSB) that provides Strategic Planning, Public Health Emergency Response, and Data Management Solutions for Federal Civilian and Defense Agencies. We have over 20 years of experience helping health and defense agencies develop concept of operations, deploy assets and personnel in Hot Zones around the world, and deliver goods and services all of the globe.</p>
  <span class="btn">Read More</span>
  <div class="about-art" role="img" aria-label="Illustration of a desk with laptop, coffee cup, phone and charts"></div>
</section>

<section class="capabilities">
  <div class="deco-ring"></div>
  <h2 class="section-title">CORE CAPABILITIES</h2>
  <article class="card" style="left:162px">
    <svg viewBox="0 0 88 80" fill="none" stroke="#1f3f5c" stroke-width="4"><circle cx="44" cy="40" r="22"/><ellipse cx="44" cy="40" rx="10" ry="22"/><path d="M22 40h44M26 29h36M26 51h36"/></svg>
    <h3>Disaster Response</h3>
    <p>Lorem ipsum dolor sit amet, consectetur adipiscing elit, sed do eiusmod temporcid idunt ut labore et dolore magn</p>
  </article>
  <article class="card" style="left:461px">
    <svg viewBox="0 0 88 80" fill="none" stroke="#1f3f5c" stroke-width="4"><path d="M14 20l10 10M24 20 14 30M60 52l10 10M70 52 60 62M56 10l10 10M66 10 56 20"/><circle cx="22" cy="60" r="5"/><path d="M27 58c14-4 10-20 26-26M46 28l8 4-2 8"/></svg>
    <h3>Strategic Planning</h3>
    <p>Lorem ipsum dolor sit amet, consectetur adipiscing elit, sed do eiusmod temporcid idunt ut labore et dolore magn</p>
  </article>
  <article class="card" style="left:759px">
    <svg viewBox="0 0 88 80" fill="none" stroke="#1f3f5c" stroke-width="4"><ellipse cx="44" cy="14" rx="22" ry="7"/><path d="M22 14v52c0 4 10 7 22 7s22-3 22-7V14M22 31c0 4 10 7 22 7s22-3 22-7M22 48c0 4 10 7 22 7s22-3 22-7"/></svg>
    <h3>Database Management</h3>
    <p>Lorem ipsum dolor sit amet, consectetur adipiscing elit, sed do eiusmod temporcid idunt ut labore et dolore magn</p>
  </article>
</section>

<section class="leadership">
  <h2 class="section-title">Leadership Team</h2>
  <div class="leader-photo" style="left:162px" role="img" aria-label="Portrait of the Chief Executive Officer"></div>
  <div class="leader-info" style="left:331px">
    <h3>Ret. SFC Marcus T. Brisco</h3>
    <div class="role">Chief Executive Office</div>
    <p>Brisco &amp; Wendell, LLC was founded by Retired Sergeant First Class (Ret. SFC) Marcus Brisco. Mr. Brisco retired from the US Army after over 20 years of service which included tours in "Operation Desert Storm/Shield", two tours of duty at the DMZ in Korea, also served in various locations in Germany including the Berlin Wall, and a Tour in Bosnia, Herzegovina for operation "Deliberate Force".</p>
  </div>
  <div class="leader-photo" style="left:624px" role="img" aria-label="Portrait of the Business Development Manager"></div>
  <div class="leader-info" style="left:793px">
    <h3>Mr. Daniel K. Ferrand</h3>
    <div class="role">Business Development Manager</div>
    <p>Mr. Ferrand brings over 10 years of business development experience to Brisco &amp; Wendell LLC. Prior to joining, Mr. Ferrand led business development capture for large and midsize defense companies in the Washington DC area servicing agencies such as the Army, US Air Force, the Defense Logistics Agency, Center for Disease Control, Food and Drug Administration and the Federal Aviation</p>
  </div>
</section>

<section class="join">
  <h2 class="section-title">JOIN US</h2>
  <p class="join-text">Brisco &amp; Wendell strives to provide an outstanding work environment for our employees. We invest in our people and believe strongly in creating an environment where our employees are free to work on innovative solutions that meet our clients' needs. We promote true work-life balance, career advancement, health, and financial security and fun in the work place. We encourage our employees to participate in our internal operation and help to develop them into the ideal consultants that our clients seek.</p>
  <span class="btn">Join Us</span>
</section>

<footer class="site-footer">
  <div class="footer-brand"><span class="brand-mark"></span>Brisco &amp; Wendell</div>
  <div class="social">
    <svg width="24" height="22" viewBox="0 0 24 22" role="img" aria-label="Email"><rect x="1" y="3" width="22" height="16" fill="#111418"/><path d="M2 4l10 8 10-8" fill="none" stroke="#fff" stroke-width="2"/></svg>
    <span role="img" aria-label="Social link"></span><span role="img" aria-label="Social link"></span><span role="img" aria-label="Social link"></span>
  </div>
  <p class="copyright">© 2018 All Rights are Reserved. Privacy Policy | Terms of Use | Contact</p>
</footer>
</body>
</html>
```